Web interface for PC desktop app

We need an HTML design for our new PC software.

To get an idea of the project scope, please review the interface draft in the attached files. The screenshot shows almost all dialogs of our product.

Our product is software that allows users to replace static Windows wallpaper with live animated scenes. The program interface consists of a gallery where users can select and download animated scenes, as well as an information area with scene details and current desktop settings. The product will be distributed on the Vexlo platform among the gamer community.

For this project, you need to create an engaging and user-friendly interface using HTML and CSS in two color schemes (black and white). Additionally, you will need to create a colorized version of the main program icon in vector format (a draft of the program icon is attached), design all other program icons, including icons for the title bar, and redraw all other images according to your design style.

Project Requirements:
-Develop a comprehensive design for the application, including icons and images, in two color schemes: dark and light.
-Colorize our main program icon according to your design style.
-Create other UI icons in all sizes from 16x16 to 512x512 pixels, ensuring that other images are suitable for up to 4K monitors.
-Ensure all UI controls have styles for standard Windows states: normal, hovered, active, and disabled.

Deliverables:
-Final design in HTML and CSS format.
-Icons in ICO format.
-Images in PNG format.

• all interface elements, including the program title bar, coded in HTML and CSS.

```html
<!DOCTYPE html>
<html lang="en">
<head>
<meta charset="utf-8">
<title>Motion Desk Studio</title>
<link href="https://fonts.googleapis.com/css2?family=Inter:wght@400;500;600;700;800&display=swap" rel="stylesheet">
<style>
:root{
  --bg:#0a0b0d;
  --host:#111316;
  --host-text:#3a3f47;
  --window:#0c0c0e;
  --panel:#131315;
  --card:#18181b;
  --card-line:#222226;
  --text:#f2f3f5;
  --muted:#8a8d93;
  --accent:#2eaef0;
  --accent-line:#3cc0ff;
  --danger:#2a1416;
}
*{box-sizing:border-box;margin:0;padding:0}
html,body{width:1200px;height:725px;overflow:hidden}
body{background:var(--bg);font-family:"Inter",sans-serif;color:var(--text);position:relative}
.abs{position:absolute}
svg{display:block}
/* host client */
.host-menu{left:10px;top:5px;display:flex;gap:16px;font-size:8px;color:var(--host-text);align-items:center}
.host-brand{display:flex;align-items:center;gap:5px}
.host-brand i{width:9px;height:9px;border-radius:50%;background:var(--host-text);display:block}
.host-nav{left:14px;top:25px;display:flex;gap:14px;font-size:12.5px;font-weight:700;color:#3b4048;align-items:center}
.host-nav .on{color:#1d4f78;border-bottom:2px solid #1d4f78;padding-bottom:1px}
.host-top-right{right:8px;top:5px;display:flex;gap:10px;align-items:center}
.host-pill{width:34px;height:16px;background:#102a40;border-radius:2px}
.host-user{font-size:8px;color:#1d4f78}
.host-side{left:0;top:57px;width:57px;height:611px;background:#0e1013}
.host-side-list{left:6px;top:62px;font-size:9px;color:#2c3138;line-height:18.2px}
.host-side-list .home{background:#15181c;padding:0 4px;margin-bottom:10px}
.host-art{left:1143px;top:95px;width:57px;height:430px;background:linear-gradient(180deg,#2a1a1e,#1a0e10 40%,#0f0b0c 60%,#241010);opacity:.7}
.host-bottom{left:0;top:698px;width:1200px;height:27px;background:#0d0f12;font-size:8.5px;color:#2c3138}
.host-bottom span{position:absolute;top:8px}
/* window */
.window{left:57px;top:57px;width:1087px;height:611px;background:var(--window);border:1px solid var(--accent-line);border-radius:2px}
.titlebar{left:0;top:0;width:100%;height:28px;display:flex;align-items:center;padding-left:10px;gap:7px;font-size:8.5px;font-weight:500}
.app-mark{width:13px;height:13px;border-radius:3px;background:var(--accent)}
.win-ctl{right:8px;top:8px;display:flex;gap:12px;color:#555}
/* left panel */
.left{left:11px;top:39px;width:306px;height:496px;background:var(--panel);border-radius:5px}
.mode-tabs{left:11px;top:12px;width:284px;height:26px;background:#161618;border-radius:4px}
.tab{position:absolute;top:0;height:26px;display:flex;align-items:center;justify-content:center;gap:6px;font-size:8.5px;border-radius:4px}
.tab.active{background:var(--accent);color:#fff}
.display{position:absolute;top:44px;width:139px;height:120px;background:var(--card);border:1px solid var(--card-line);border-radius:4px}
.display.active{border-color:var(--accent-line)}
.display .thumb{position:absolute;left:11px;top:11px;width:116px;height:62px;border-radius:6px}
.display .label{position:absolute;left:11px;top:86px;font-size:8px;color:var(--muted)}
.display .model{position:absolute;left:11px;top:100px;font-size:8.5px}
.btn{position:absolute;height:26px;display:flex;align-items:center;gap:8px;padding-left:6px;font-size:8.5px;background:#161618;border:1px solid var(--card-line);border-radius:13px}
.btn .ico{width:16px;height:16px;border-radius:50%;background:#1f1f23;display:flex;align-items:center;justify-content:center}
.preview{left:11px;top:208px;width:283px;height:240px;background:var(--panel);border:1px solid var(--card-line);border-radius:4px}
.preview h3{position:absolute;left:11px;top:8px;font-size:8.5px;font-weight:500}
.preview .art{position:absolute;left:11px;top:22px;width:261px;height:105px;border-radius:2px;background:linear-gradient(180deg,#1d2a4e 0%,#27335a 40%,#1a2236 70%,#2a1f30 100%)}
.meta{position:absolute;font-size:8px}
.meta b{display:block;font-weight:400;color:var(--muted);margin-bottom:6px}
.meta span{font-size:8.5px}
.stars{color:var(--accent);letter-spacing:1px;font-size:7px}
.stars em{color:#fff;font-style:normal}
.action{position:absolute;top:202px;height:26px;display:flex;align-items:center;font-size:8.5px;background:#161618;border:1px solid var(--card-line);border-radius:3px}
.action .ico{width:20px;height:24px;display:flex;align-items:center;justify-content:center;border-right:1px solid var(--card-line);margin-right:9px}
.action.danger{background:var(--danger)}
.create{left:11px;top:460px;width:284px;height:25px;background:#161618;border-radius:4px;font-size:8.5px}
.create .plus{position:absolute;left:3px;top:3px;width:19px;height:19px;border:1px solid var(--card-line);border-radius:3px;display:flex;align-items:center;justify-content:center}
.create span{position:absolute;left:0;width:100%;text-align:center;top:7px}
/* right */
.rtab{position:absolute;top:40px;height:26px;display:flex;align-items:center;font-size:8.5px;border-radius:4px;background:#131315}
.rtab .ico{position:absolute;left:2px;top:3px;width:20px;height:20px;border:1px solid #26262a;border-radius:3px;display:flex;align-items:center;justify-content:center}
.rtab.active{background:var(--accent)}
.rtab.active .ico{border-color:#8fd8ff}
.rtab span{width:100%;text-align:center}
.gallery{left:328px;top:77px;width:740px;height:523px;background:var(--panel);border-radius:5px;overflow:hidden}
.search{left:11px;top:11px;width:153px;height:26px;background:#18181b;border:1px solid var(--card-line);border-radius:3px;display:flex;align-items:center;gap:10px;padding-left:8px;font-size:8.5px}
.filter{position:absolute;top:11px;height:26px;background:#18181b;border:1px solid var(--card-line);border-radius:3px;display:flex;align-items:center;font-size:8.5px}
.filter .ico{width:20px;height:24px;display:flex;align-items:center;justify-content:center;border-right:1px solid var(--card-line);margin:0 8px 0 2px}
.filter .chev{position:absolute;right:10px;top:9px}
.row-title{position:absolute;left:11px;font-size:17px;font-weight:700;letter-spacing:-.2px}
.pager{position:absolute;width:25px;height:25px;background:#1b1b1e;border-radius:3px;display:flex;align-items:center;justify-content:center}
.strip{position:absolute;left:11px;height:113px;width:723px;overflow:hidden}
.tile{position:absolute;top:0;width:170px;height:113px;border-radius:2px}
.t1{background:linear-gradient(160deg,#2c3350 0%,#1c2640 45%,#3a2c20 80%,#17161c)}
.t2{background:linear-gradient(180deg,#3f6768 0%,#2a4a4c 50%,#1a2a2c 100%)}
.t3{background:linear-gradient(180deg,#8c6a98 0%,#c27a92 45%,#4a3a50 80%,#221a24)}
.t4{background:linear-gradient(180deg,#e8583a 0%,#f08a52 35%,#5a3a4a 70%,#1e2434)}
.scrollbar{left:1074px;top:79px;width:2px;height:170px;background:#2b6e93;border-radius:1px}
</style>
</head>
<body>

<!-- host client behind the window -->
<div class="abs host-menu"><span class="host-brand"><i></i>Vexlo</span><span>View</span><span>Friends</span><span>Games</span><span>Help</span></div>
<div class="abs host-top-right"><div class="host-pill"></div><span class="host-user">Novakit</span></div>
<div class="abs host-nav">
  <svg width="10" height="10" viewBox="0 0 10 10"><path d="M8 5H2M5 2 2 5l3 3" stroke="#3b4048" fill="none" stroke-width="1.4"/></svg>
  <svg width="10" height="10" viewBox="0 0 10 10"><path d="M2 5h6M5 2l3 3-3 3" stroke="#2a2e35" fill="none" stroke-width="1.4"/></svg>
  <span>STORE</span><span class="on">LIBRARY</span><span>COMMUNITY</span><span>NOVAKIT</span>
</div>
<div class="abs host-side"></div>
<div class="abs host-side-list">
  <div class="home">Home</div><div>Games</div><div>&nbsp;</div><div>— ALL</div>
  <div>Crossh</div><div>Crab</div><div>Dustl</div><div>Dustl</div><div>Dustl</div><div>Titan</div><div>Titan</div><div>Ironf</div><div>World</div>
</div>
<div class="abs host-art" role="img" aria-label="Dimmed game artwork on the library page"></div>
<div class="abs host-bottom"><span style="left:28px">Add a Game</span><span style="left:636px">Manage Downloads</span></div>

<!-- application window -->
<div class="abs window">
  <div class="abs titlebar"><div class="app-mark"></div>Motion Desk Studio</div>
  <div class="abs win-ctl">
    <svg width="8" height="8" viewBox="0 0 8 8"><path d="M1 4.5h6" stroke="#555"/></svg>
    <svg width="8" height="8" viewBox="0 0 8 8"><rect x="1" y="1" width="6" height="6" fill="none" stroke="#555"/></svg>
    <svg width="8" height="8" viewBox="0 0 8 8"><path d="M1 1l6 6M7 1 1 7" stroke="#777"/></svg>
  </div>

  <section class="abs left">
    <div class="abs mode-tabs">
      <div class="tab active" style="left:0;width:142px">
        <svg width="10" height="10" viewBox="0 0 10 10"><rect x=".8" y=".8" width="8.4" height="8.4" rx="2" fill="none" stroke="#fff"/><circle cx="3.5" cy="3.6" r="1" fill="#fff"/><path d="M1.5 8 4.5 5.5 8.5 8" stroke="#fff" fill="none"/></svg>Wallpapers</div>
      <div class="tab" style="left:142px;width:142px">
        <svg width="11" height="10" viewBox="0 0 11 10"><rect x=".8" y=".8" width="9.4" height="6.5" rx="1.5" fill="none" stroke="#fff"/><path d="M3.5 9h4" stroke="#fff"/></svg>Screensavers</div>
    </div>

    <div class="display active" style="left:11px">
      <div class="thumb t1" role="img" aria-label="Pixel art night city thumbnail"></div>
      <div class="label">Display 1</div><div class="model">Lumora L24HD</div>
    </div>
    <div class="display" style="left:156px">
      <div class="thumb" style="background:linear-gradient(180deg,#1f3330,#16211f 60%,#2a1a1c)" role="img" aria-label="Pixel art rainy green city thumbnail"></div>
      <div class="label">Display 2</div><div class="model">Lumora F23HD</div>
    </div>

    <div class="btn" style="left:11px;top:171px;width:77px"><span class="ico"><svg width="9" height="9" viewBox="0 0 10 10"><circle cx="5" cy="5" r="1.6" fill="none" stroke="#fff"/><circle cx="5" cy="5" r="3.8" fill="none" stroke="#fff" stroke-dasharray="2 1"/></svg></span>Settings</div>
    <div class="btn" style="left:83px;top:171px;width:62px;left:94px"><span class="ico"><svg width="8" height="8" viewBox="0 0 8 8"><path d="M2 1l5 3-5 3z" fill="none" stroke="#fff"/></svg></span>Play</div>
    <div class="btn" style="left:161px;top:171px;width:63px"><span class="ico"><svg width="8" height="8" viewBox="0 0 8 8"><rect x="1" y="1" width="6" height="6" rx="1.5" fill="none" stroke="#fff"/></svg></span>Stop</div>
    <div class="btn" style="left:230px;top:171px;width:64px"><span class="ico"><svg width="8" height="8" viewBox="0 0 8 8"><path d="M2.5 1v6M5.5 1v6" stroke="#fff"/></svg></span>Pause</div>

    <div class="abs preview">
      <h3>Preview</h3>
      <div class="art" role="img" aria-label="Pixel art rainy night city street with neon signs"></div>
      <div class="meta" style="left:11px;top:140px"><b>Wallpaper Name</b><span>Neon Alley Rain</span></div>
      <div class="meta" style="left:92px;top:140px"><b>Author Name</b><span>Pixel Drift</span></div>
      <div class="meta" style="left:165px;top:140px"><b>Resolution</b><span>3840×2400</span></div>
      <div class="meta" style="left:11px;top:172px"><b>Size</b><span>#nAn MB</span></div>
      <div class="meta" style="left:62px;top:172px"><b>Rating</b><span class="stars">★★★★<em>★</em></span></div>
      <div class="action" style="left:11px;width:68px"><span class="ico"><svg width="8" height="9" viewBox="0 0 8 9"><path d="M4 8V1M1 4l3-3 3 3" stroke="#fff" fill="none"/></svg></span>Apply</div>
      <div class="action" style="left:85px;width:62px"><span class="ico"><svg width="9" height="10" viewBox="0 0 9 10"><path d="M4.5 1 8 2.5v3c0 2-1.7 3.2-3.5 3.8C2.7 8.7 1 7.5 1 5.5v-3z" fill="none" stroke="#fff"/></svg></span>Test</div>
      <div class="action danger" style="left:194px;width:78px"><span class="ico" style="border-color:#3a2024"><svg width="8" height="9" viewBox="0 0 8 9"><path d="M1 2h6M3 2V1h2v1M1.8 2l.5 6h3.4l.5-6" stroke="#fff" fill="none"/></svg></span>Uninstall</div>
    </div>

    <div class="abs create">
      <div class="plus"><svg width="8" height="8" viewBox="0 0 8 8"><path d="M4 0v8M0 4h8" stroke="#fff"/></svg></div>
      <span>Create your own wallpaper</span>
    </div>
  </section>

  <!-- top tabs right -->
  <div class="rtab" style="left:329px;width:151px"><span class="ico"><svg width="10" height="10" viewBox="0 0 10 10"><rect x=".8" y=".8" width="8.4" height="8.4" rx="2" fill="none" stroke="#fff"/><circle cx="3.5" cy="3.6" r="1" fill="#fff"/><path d="M1.5 8 4.5 5.5 8.5 8" stroke="#fff" fill="none"/></svg></span><span>Installed</span></div>
  <div class="rtab active" style="left:484px;width:138px"><span class="ico"><svg width="11" height="10" viewBox="0 0 11 10"><rect x=".8" y=".8" width="9.4" height="6.5" rx="1.5" fill="none" stroke="#fff"/><path d="M3.5 9h4" stroke="#fff"/></svg></span><span>Workshop</span></div>
  <div class="rtab" style="left:905px;width:77px;justify-content:flex-start;padding-left:29px"><span class="ico"><svg width="10" height="10" viewBox="0 0 10 10"><circle cx="5" cy="5" r="1.6" fill="none" stroke="#fff"/><circle cx="5" cy="5" r="3.8" fill="none" stroke="#fff" stroke-dasharray="2 1"/></svg></span>Settings</div>
  <div class="rtab" style="left:990px;width:78px;justify-content:flex-start;padding-left:29px"><span class="ico"><svg width="9" height="10" viewBox="0 0 9 10"><circle cx="4.5" cy="3" r="2" fill="none" stroke="#fff"/><path d="M1 9.5c0-2 1.5-3.3 3.5-3.3S8 7.5 8 9.5z" fill="none" stroke="#fff"/></svg></span>Account</div>

  <section class="abs gallery">
    <div class="abs search"><svg width="10" height="10" viewBox="0 0 10 10"><circle cx="4.3" cy="4.3" r="3.3" fill="none" stroke="#fff"/><path d="M6.8 6.8 9.3 9.3" stroke="#fff"/></svg>Search wallpaper...</div>
    <div class="filter" style="left:409px;width:102px"><span class="ico"><svg width="8" height="8" viewBox="0 0 8 8"><g fill="none" stroke="#fff" stroke-width=".9"><rect x=".5" y=".5" width="2.8" height="2.8" rx=".8"/><rect x="4.7" y=".5" width="2.8" height="2.8" rx=".8"/><rect x=".5" y="4.7" width="2.8" height="2.8" rx=".8"/><rect x="4.7" y="4.7" width="2.8" height="2.8" rx=".8"/></g></svg></span>Category<svg class="chev" width="8" height="6" viewBox="0 0 8 6"><path d="M1 1.5 4 4.5 7 1.5" stroke="#fff" fill="none"/></svg></div>
    <div class="filter" style="left:520px;width:103px"><span class="ico"><svg width="9" height="8" viewBox="0 0 9 8"><path d="M0 2h9M0 6h9" stroke="#fff"/><circle cx="3" cy="2" r="1.2" fill="#18181b" stroke="#fff"/><circle cx="6" cy="6" r="1.2" fill="#18181b" stroke="#fff"/></svg></span>All<svg class="chev" width="8" height="6" viewBox="0 0 8 6"><path d="M1 1.5 4 4.5 7 1.5" stroke="#fff" fill="none"/></svg></div>
    <div class="filter" style="left:632px;width:102px"><span class="ico"><svg width="9" height="9" viewBox="0 0 10 10"><path d="M5 .5 6.4 3.6 9.6 3.8 7.1 5.9 7.9 9.2 5 7.4 2.1 9.2 2.9 5.9.4 3.8 3.6 3.6z" fill="#fff"/></svg></span>Top Rated<svg class="chev" width="8" height="6" viewBox="0 0 8 6"><path d="M1 1.5 4 4.5 7 1.5" stroke="#fff" fill="none"/></svg></div>

    <!-- row 1 -->
    <div class="row-title" style="top:116px">Featured</div>
    <div class="pager" style="left:674px;top:106px"><svg width="6" height="8" viewBox="0 0 6 8"><path d="M4.5 1 1.5 4l3 3" stroke="#fff" fill="none"/></svg></div>
    <div class="pager" style="left:708px;top:106px"><svg width="6" height="8" viewBox="0 0 6 8"><path d="M1.5 1l3 3-3 3" stroke="#fff" fill="none"/></svg></div>
    <div class="strip" style="top:138px">
      <div class="tile t1" style="left:0" role="img" aria-label="Pixel art night city with lit windows"></div>
      <div class="tile t2" style="left:176px" role="img" aria-label="Pixel art teal rainy rooftops with power lines"></div>
      <div class="tile t3" style="left:351px" role="img" aria-label="Pixel art pink dusk skyline with full moon"></div>
      <div class="tile t4" style="left:527px" role="img" aria-label="Pixel art orange sunset over city towers"></div>
      <div class="tile t1" style="left:702px" role="img" aria-label="Pixel art night city"></div>
    </div>

    <!-- row 2 -->
    <div class="row-title" style="top:272px">Featured</div>
    <div class="pager" style="left:674px;top:262px"><svg width="6" height="8" viewBox="0 0 6 8"><path d="M4.5 1 1.5 4l3 3" stroke="#fff" fill="none"/></svg></div>
    <div class="pager" style="left:708px;top:262px"><svg width="6" height="8" viewBox="0 0 6 8"><path d="M1.5 1l3 3-3 3" stroke="#fff" fill="none"/></svg></div>
    <div class="strip" style="top:294px">
      <div class="tile t1" style="left:0" role="img" aria-label="Pixel art night city with lit windows"></div>
      <div class="tile t2" style="left:176px" role="img" aria-label="Pixel art teal rainy rooftops with power lines"></div>
      <div class="tile t3" style="left:351px" role="img" aria-label="Pixel art pink dusk skyline with full moon"></div>
      <div class="tile t4" style="left:527px" role="img" aria-label="Pixel art orange sunset over city towers"></div>
      <div class="tile t1" style="left:702px" role="img" aria-label="Pixel art night city"></div>
    </div>

    <!-- row 3 -->
    <div class="row-title" style="top:428px">Featured</div>
    <div class="pager" style="left:674px;top:418px"><svg width="6" height="8" viewBox="0 0 6 8"><path d="M4.5 1 1.5 4l3 3" stroke="#fff" fill="none"/></svg></div>
    <div class="pager" style="left:708px;top:418px"><svg width="6" height="8" viewBox="0 0 6 8"><path d="M1.5 1l3 3-3 3" stroke="#fff" fill="none"/></svg></div>
    <div class="strip" style="top:450px">
      <div class="tile t1" style="left:0" role="img" aria-label="Pixel art night city with lit windows"></div>
      <div class="tile t2" style="left:176px" role="img" aria-label="Pixel art teal rainy rooftops with power lines"></div>
      <div class="tile t3" style="left:351px" role="img" aria-label="Pixel art pink dusk skyline with full moon"></div>
      <div class="tile t4" style="left:527px" role="img" aria-label="Pixel art orange sunset over city towers"></div>
      <div class="tile t1" style="left:702px" role="img" aria-label="Pixel art night city"></div>
    </div>
  </section>
  <div class="abs scrollbar"></div>
</div>
</body>
</html>
```